A online shop for solid wood need a Stationary design

A new online shop (in Austria and Germany) for solid wood and steel furniture (feldberg-formwerk) needs a Stationay design (letterhead, business card, envelope etc...). Dining tables, coffee tables, TV furniture and similar furniture will be sold. Everything will be custom made.

```html
<!DOCTYPE html>
<html lang="en">
<head>
<meta charset="utf-8">
<title>Feldberg Formwerk – Stationery Set</title>
<link rel="stylesheet" href="https://fonts.googleapis.com/css2?family=Montserrat:wght@400;500;600;700;800&display=swap">
<style>
  :root {
    --backdrop: #6d7e7f;
    --paper: #f7f9f8;
    --red: #ff0000;
    --red-dark: #b00000;
    --ink: #3a4448;
    --text: #646c70;
    --muted: #8c9599;
  }
  * { box-sizing: border-box; margin: 0; padding: 0; }
  html, body { width: 1200px; height: 1189px; overflow: hidden; }
  body {
    background: var(--backdrop);
    font-family: "Montserrat", sans-serif;
    color: var(--ink);
    position: relative;
  }
  .sheet { position: absolute; background: var(--paper); overflow: hidden; }
  .abs { position: absolute; }

  /* corner border areas: soft red gradient fills */
  .border-fill { position: absolute; }
  .border-fill--top-right { top: 0; right: 0; border-bottom-left-radius: 100% 100%; background: linear-gradient(210deg, var(--red) 35%, var(--red-dark)); }
  .border-fill--top-left { top: 0; left: 0; border-bottom-right-radius: 100% 100%; background: linear-gradient(150deg, var(--red) 35%, var(--red-dark)); }
  .border-fill--bottom-left { bottom: 0; left: 0; border-top-right-radius: 100% 100%; background: linear-gradient(30deg, var(--red) 35%, var(--red-dark)); }
  .border-fill--bottom-right { bottom: 0; right: 0; border-top-left-radius: 100% 100%; background: linear-gradient(330deg, var(--red) 35%, var(--red-dark)); }
  .border-fill--pale { background: linear-gradient(210deg, #d4dad9, #aeb6b5); }

  /* brand name block */
  .brand { position: absolute; display: flex; flex-direction: column; align-items: center; text-align: center; }
  .brand-square { background: var(--red); margin-bottom: 6px; }
  .brand-name { color: var(--red); font-weight: 800; line-height: 1.05; letter-spacing: 0.04em; }
  .brand--white .brand-square { background: #fff; }
  .brand--white .brand-name { color: #fff; }

  /* letterhead */
  .letterhead { left: 71px; top: 81px; width: 500px; height: 710px; }
  .letterhead .sender { left: 58px; top: 168px; font-size: 12.5px; line-height: 16px; color: var(--ink); }
  .rule { position: absolute; height: 2px; background: var(--ink); }
  .letterhead .headline { left: 57px; top: 239px; font-size: 16.5px; font-weight: 600; letter-spacing: 0.01em; color: var(--ink); }
  .letterhead .body-copy { left: 57px; font-size: 9.7px; line-height: 20.6px; color: var(--text); white-space: nowrap; }
  .letterhead .closing { left: 58px; font-size: 12px; color: var(--ink); }
  .letterhead .signature { right: 65px; top: 530px; text-align: right; font-size: 12.5px; line-height: 17px; }
  .signature strong { font-weight: 700; }
  .signature .site { color: var(--muted); font-size: 10.5px; }

  /* invoice */
  .invoice { left: 628px; top: 84px; width: 501px; height: 711px; }
  .invoice-title { left: 289px; top: 126px; font-size: 36.5px; font-weight: 800; color: var(--red); letter-spacing: 0.01em; line-height: 1.1; }
  .invoice-meta { left: 283px; top: 169px; width: 174px; border: 1.5px solid var(--ink); font-size: 10.5px; font-weight: 600; }
  .invoice-meta div { display: flex; justify-content: space-between; padding: 2px 7px; height: 18.5px; }
  .invoice-meta div + div { border-top: 1.5px solid var(--ink); }
  .line-items { left: 37px; top: 235px; width: 428px; }
  .row { display: grid; align-items: center; font-size: 11.5px; color: var(--ink); }
  .row span:nth-child(2), .row span:nth-child(3), .row span:nth-child(4) { text-align: center; }
  .row--head { height: 25px; background: var(--red); color: #fff; border-radius: 13px; font-size: 12.5px; font-weight: 600; grid-template-columns: 200px 90px 50px 88px; }
  .row--head span:nth-child(1) { padding-left: 25px; }
  .row--item { height: 36.8px; margin: 0 17px 0 16px; border-bottom: 1.3px solid var(--ink); grid-template-columns: 184px 90px 50px 71px; }
  .row--item span:nth-child(1) { padding-left: 28px; }
  .row--item span:nth-child(4) { text-align: right; }
  .bill-to { left: 61px; top: 459px; font-size: 8.4px; line-height: 16.2px; color: var(--ink); }
  .bill-to h3 { color: var(--red); font-size: 11px; font-weight: 700; line-height: 16px; }
  .bill-to .gap { margin-top: 2px; }
  .bill-to b { font-weight: 700; }
  .totals { left: 258px; top: 458px; width: 184px; font-size: 11.5px; }
  .totals div { display: flex; justify-content: space-between; height: 20.5px; align-items: center; }
  .grand-total { left: 236px; top: 526px; width: 229px; height: 25px; border-radius: 13px; background: var(--red); color: #fff; font-size: 11.5px; font-weight: 600; display: flex; justify-content: space-between; align-items: center; padding: 0 23px; }
  .terms { left: 61px; top: 625px; }
  .terms h3 { font-size: 10px; font-weight: 700; color: var(--ink); margin-bottom: 4px; }
  .terms p { font-size: 7.3px; line-height: 14px; color: var(--muted); white-space: nowrap; }

  /* business cards */
  .card-front { left: 70px; top: 826px; width: 238px; height: 154px; background: var(--red); }
  .card-back { left: 334px; top: 913px; width: 237px; height: 154px; }
  .card-back .holder { right: 22px; top: 36px; text-align: right; }
  .holder .name { font-size: 12px; color: var(--red); letter-spacing: 0.01em; }
  .holder .name b { font-weight: 700; }
  .holder .role { font-size: 4.6px; color: var(--muted); letter-spacing: 0.05em; }
  .contact-list { left: 19px; top: 82px; list-style: none; }
  .contact-list li { display: flex; align-items: center; height: 14.4px; font-size: 4.6px; color: var(--muted); letter-spacing: 0.03em; }
  .contact-list svg { width: 11px; height: 11px; margin-right: 6px; }

  /* envelope */
  .envelope { left: 625px; top: 850px; width: 500px; height: 257px; }
  .address-box { left: 233px; top: 181px; width: 229px; height: 42px; background: #fff; border-radius: 10px; display: flex; align-items: center; padding-left: 11px; gap: 13px; }
  .address-box .to-name { font-size: 10.5px; color: var(--ink); }
  .address-box .to-name b { font-weight: 700; }
  .address-box .to-address { font-size: 9.3px; line-height: 13px; color: var(--text); }
</style>
</head>
<body>

<!-- Letterhead -->
<section class="sheet letterhead">
  <div class="border-fill border-fill--top-right" style="width:273px;height:155px" role="img" aria-label="Red wave border, top right corner"></div>
  <div class="border-fill border-fill--bottom-left" style="width:230px;height:130px" role="img" aria-label="Red wave border, bottom left corner"></div>

  <div class="brand" style="left:30px;top:52px;width:140px">
    <div class="brand-square" style="width:24px;height:24px"></div>
    <div class="brand-name" style="font-size:15px">FELDBERG<br>FORMWERK</div>
  </div>

  <p class="abs sender">Street Location<br>yourname@mail.com</p>
  <div class="rule" style="left:57px;top:209px;width:143px"></div>

  <h1 class="abs headline">SUBJECT HEADLINE HERE</h1>
  <p class="abs body-copy" style="top:269px">Lorem ipsum dolor sit amet, consectetuer adipiscing elit, sed diam<br>nonummy nibh euismod tincidunt ut laoreet dolore magna aliquam erat<br>volutpat. Ut wisi enim ad minim veniam, quis nostrud exerci tation</p>
  <p class="abs body-copy" style="top:343px">Lorem ipsum dolor sit amet, consectetuer adipiscing elit, sed diam<br>nonummy nibh euismod tincidunt ut laoreet dolore magna aliquam erat<br>volutpat. Ut wisi enim ad minim veniam, quis nostrud exerci tation<br>ullamcorper suscipit lobortis nisl ut aliquip ex ea commodo consequat. Duis<br>autem vel eum iriure dolor in hendrerit in vulputate velit esse molestie<br>consequat, vel illum dolore eu feugiat nulla facilisis at vero eros et accumsan</p>

  <p class="abs closing" style="top:505px">Regard</p>
  <p class="abs closing" style="top:571px">Lorem Ipsum</p>

  <div class="abs signature">
    <strong>Your Name</strong><br>
    Street Location<br>
    <span class="site">www.yourwebsite.com</span>
  </div>
  <div class="rule" style="left:302px;top:585px;width:131px;height:1.5px"></div>
</section>

<!-- Invoice -->
<section class="sheet invoice">
  <div class="border-fill border-fill--top-left" style="width:274px;height:155px" role="img" aria-label="Red wave border, top left corner"></div>
  <div class="border-fill border-fill--bottom-right" style="width:204px;height:118px" role="img" aria-label="Red wave border, bottom right corner"></div>

  <div class="brand" style="left:54px;top:122px;width:140px">
    <div class="brand-square" style="width:24px;height:24px"></div>
    <div class="brand-name" style="font-size:15px">FELDBERG<br>FORMWERK</div>
  </div>

  <h1 class="abs invoice-title">INVOICE</h1>
  <div class="abs invoice-meta">
    <div><span>Invoice:</span><span>123456</span></div>
    <div><span>Date:</span><span>14 Februari 2020</span></div>
  </div>

  <div class="abs line-items">
    <div class="row row--head"><span>Product Description</span><span>Price</span><span>Qty.</span><span>Total</span></div>
    <div class="row row--item"><span>Product Description</span><span>$10.00</span><span>1</span><span>$10.00</span></div>
    <div class="row row--item"><span>Product Description</span><span>$10.00</span><span>1</span><span>$10.00</span></div>
    <div class="row row--item"><span>Product Description</span><span>$10.00</span><span>1</span><span>$10.00</span></div>
    <div class="row row--item"><span>Product Description</span><span>$10.00</span><span>1</span><span>$10.00</span></div>
    <div class="row row--item"><span>Product Description</span><span>$10.00</span><span>1</span><span>$10.00</span></div>
  </div>

  <div class="abs bill-to">
    <h3>Invoice to:</h3>
    <b>Name Surename</b><br>
    Addrees<br>
    +123 456 789<br>
    yourname@mail.com
    <h3 class="gap">Payment Info:</h3>
    Account No: 0123456789<br>
    Name: Mara Lindt<br>
    Bank Detail: 0123 456 789
  </div>

  <div class="abs totals">
    <div><span>Subtotal</span><span>$50.00</span></div>
    <div><span>Shipping</span><span>$15.00</span></div>
    <div><span>Tax Rate</span><span>$1.00</span></div>
  </div>
  <div class="abs grand-total"><span>GRAND TOTAL</span><span>$66.00</span></div>

  <div class="rule" style="left:53px;top:615px;width:207px;height:1.5px"></div>
  <div class="abs terms">
    <h3>Term &amp; Conditions:</h3>
    <p>Lorem ipsum dolor sit amet, consectetuer adipiscing<br>elit, sed diam nonummy nibh euismod tincidunt ut<br>laoreet dolore magna aliquam erat volutpat.</p>
  </div>
</section>

<!-- Business card front -->
<section class="sheet card-front">
  <div class="border-fill border-fill--top-right border-fill--pale" style="width:78px;height:40px" role="img" aria-label="Pale wave border, top right corner"></div>
  <div class="border-fill border-fill--bottom-left border-fill--pale" style="width:134px;height:78px" role="img" aria-label="Pale wave border, bottom left corner"></div>
  <div class="brand brand--white" style="left:59px;top:48px;width:120px">
    <div class="brand-square" style="width:20px;height:20px"></div>
    <div class="brand-name" style="font-size:12.5px">FELDBERG<br>FORMWERK</div>
  </div>
</section>

<!-- Business card back -->
<section class="sheet card-back">
  <div class="border-fill border-fill--top-left" style="width:94px;height:45px" role="img" aria-label="Red wave border, top left corner"></div>
  <div class="border-fill border-fill--bottom-right" style="width:137px;height:61px" role="img" aria-label="Red wave border, bottom right corner"></div>
  <div class="abs holder">
    <div class="name">YOURNAME<b>HERE</b></div>
    <div class="role">YOUR POSITION HERE</div>
  </div>
  <ul class="abs contact-list">
    <li><svg viewBox="0 0 12 12"><circle cx="6" cy="6" r="6" fill="var(--red)"/><rect x="3" y="4" width="6" height="4.2" fill="none" stroke="#fff" stroke-width="0.9"/><path d="M3 4 L6 6.3 L9 4" fill="none" stroke="#fff" stroke-width="0.9"/></svg>YOUR@MAIL.COM</li>
    <li><svg viewBox="0 0 12 12"><circle cx="6" cy="6" r="6" fill="var(--red)"/><path d="M4 3 L5.2 4.6 L4.6 5.4 C5 6.4 5.7 7.1 6.6 7.5 L7.4 6.8 L9 8 L8.2 9 C6 9 3 6 3 3.8 Z" fill="#fff"/></svg>+001 123 456 7890</li>
    <li><svg viewBox="0 0 12 12"><circle cx="6" cy="6" r="6" fill="var(--red)"/><path d="M6 2.5 C4.6 2.5 3.7 3.5 3.7 4.8 C3.7 6.5 6 9.5 6 9.5 C6 9.5 8.3 6.5 8.3 4.8 C8.3 3.5 7.4 2.5 6 2.5 Z" fill="#fff"/><circle cx="6" cy="4.8" r="0.9" fill="var(--red)"/></svg>YOUR ADDRESS HERE</li>
    <li><svg viewBox="0 0 12 12"><circle cx="6" cy="6" r="6" fill="var(--red)"/><circle cx="6" cy="6" r="3" fill="none" stroke="#fff" stroke-width="0.8"/><path d="M3 6 H9 M6 3 V9" stroke="#fff" stroke-width="0.7"/></svg>YOUR WEBSITE HERE</li>
  </ul>
</section>

<!-- Envelope -->
<section class="sheet envelope">
  <div class="border-fill border-fill--top-right" style="width:175px;height:100px" role="img" aria-label="Red wave border, top right corner"></div>
  <div class="border-fill border-fill--bottom-left" style="width:257px;height:156px" role="img" aria-label="Red wave border, bottom left corner"></div>
  <div class="brand" style="left:19px;top:28px;width:100px">
    <div class="brand-square" style="width:16px;height:16px;margin-bottom:4px"></div>
    <div class="brand-name" style="font-size:10.5px">FELDBERG<br>FORMWERK</div>
  </div>
  <div class="abs address-box">
    <div class="to-name">YOURNAME<b>HERE</b></div>
    <div class="to-address">Address Line Example<br>Street, DC, USA</div>
  </div>
</section>

</body>
</html>
```